The best Social Research house in LatinAmerica needs a Business Card

We need a greeting card that does justice to our everyday work. Lumenta Civica is a group of highly selected social academic minds (6 academicians selected among 800+ candidates) that analyses the field work done by our network of 56 social anthropologists in 7 Latin American countries. We spend months studying different social phenomena or groups of people and then translate the findings into powerful insights and strategic marketing actions for our clients (from Banks to TV networks, from top worldwide consumer product Companies to Government policy design or even new product innovation initiatives). We translate social academic knowledge into tangible actions. We already have a logo and we like it, but remain open for new and different proposals on size or form. We do something very different and we need a card as different as we are.
Target Market(s)
Top Management from Top Companies that need (and like) to be surprised!
Industry/Entity Type
Marketing
Look and feel

```html
<!DOCTYPE html>
<html lang="es">
<head>
<meta charset="utf-8">
<title>Lumenta Civica – Business Card</title>
<link rel="stylesheet" href="https://fonts.googleapis.com/css2?family=Arvo:wght@400;700&display=swap">
<style>
  :root {
    --bg: #e9e6e1;
    --card-white: #ffffff;
    --card-teal: #0a8f73;
    --teal-deep: #087a62;
    --leaf-green: #6ab23a;
    --text-light: #ffffff;
    --shadow: rgba(40, 30, 20, 0.22);
  }
  * { box-sizing: border-box; margin: 0; padding: 0; }
  html, body {
    width: 1200px;
    height: 900px;
    overflow: hidden;
    background: var(--bg);
    font-family: "Arvo", Georgia, serif;
  }
  .canvas {
    position: relative;
    width: 1200px;
    height: 900px;
  }
  .card {
    position: absolute;
    left: 320px;
    width: 560px;
    height: 320px;
    border-radius: 26px;
    box-shadow: 0 10px 26px var(--shadow);
    overflow: hidden;
  }
  /* Front side */
  .card--front {
    top: 90px;
    background: var(--card-white);
  }
  .front-mark {
    position: absolute;
    left: 40px;
    top: 110px;
    width: 100px;
    height: 100px;
    border-radius: 50%;
    background: var(--leaf-green);
  }
  .front-name {
    position: absolute;
    right: 34px;
    bottom: 34px;
    font-weight: 700;
    font-size: 40px;
    letter-spacing: -0.5px;
    color: var(--card-teal);
  }
  /* Back side */
  .card--back {
    top: 480px;
    background: var(--card-teal);
    color: var(--text-light);
  }
  .brand {
    position: absolute;
    left: 34px;
    top: 30px;
    display: flex;
    align-items: center;
    gap: 14px;
  }
  .brand-dot {
    width: 44px;
    height: 44px;
    border-radius: 50%;
    background: var(--leaf-green);
  }
  .brand-name {
    font-weight: 700;
    font-size: 38px;
    letter-spacing: -0.5px;
    color: var(--text-light);
  }
  .person {
    position: absolute;
    left: 40px;
    top: 132px;
  }
  .person-name {
    font-size: 26px;
    font-weight: 400;
    letter-spacing: 0.5px;
  }
  .person-role {
    font-size: 16px;
    margin-top: 4px;
  }
  .contact {
    position: absolute;
    left: 40px;
    bottom: 30px;
    font-size: 15px;
    line-height: 1.55;
    list-style: none;
  }
  .contact-label {
    display: inline-block;
    width: 20px;
  }
</style>
</head>
<body>
<main class="canvas">
  <section class="card card--front" aria-label="Card front">
    <div class="front-mark"></div>
    <div class="front-name">Lumenta Civica</div>
  </section>

  <section class="card card--back" aria-label="Card back">
    <div class="brand">
      <span class="brand-dot"></span>
      <span class="brand-name">Lumenta Civica</span>
    </div>
    <div class="person">
      <h1 class="person-name">Tomas Arbeleche</h1>
      <p class="person-role">Gabinete de Análisis</p>
    </div>
    <ul class="contact">
      <li><span class="contact-label">t</span>(55) 5210 4417</li>
      <li><span class="contact-label">e</span>tomas.arbeleche@lumenta-civica.com</li>
      <li>Calle Olmo 14. Col. Roma, Mexico DF 06700. MX.</li>
    </ul>
  </section>
</main>
</body>
</html>
```